Redesign (8 documents) attached with brand guidelines - very quick/easy job!

We have 8 flyers/documents that we need put into the style of our new brand (see attached). So this is a simple rebrand exercise - complete with our brand guidelines (see attached)

I would need the designer to sign an NDA prior to taking this piece of work as I will be sharing newly branded documents with you prior to market release.

If these are done well we would as the same designer to work on a z-card designed brochure/POS

Brief:

- These are documents that customers would need to complete in order to book a particular service
- If you use images (ideally from Pixvane, so we don’t have to pay for them!)
- Icon ideas enclosed
-All the content on the brochures is required: but if you think it would 'flow better' in a different order that is fine.

Target Market(s)

Customers interested in receiving a particular service

Industry/Entity Type

Work

Other font styles liked:
• Brandon (see brand guide)

Requirements
Must have
• A4
Nice to have
• New logo ideas
Should not have
• Anything out of brand guidleines

```html
<!DOCTYPE html>
<html lang="en">
<head>
<meta charset="utf-8">
<title>Verdalia – Client Forms</title>
<link href="https://fonts.googleapis.com/css2?family=Nunito+Sans:wght@400;600;700;800&display=swap" rel="stylesheet">
<style>
:root{
  --teal:#00a9c7;
  --yellow:#f3ef1c;
  --lime:#a8cf3a;
  --ink:#3d3d3d;
  --muted:#6b6b6b;
  --rule:#c9c9c9;
  --paper:#ffffff;
  --ground:#dcdcdc;
  --tint:#dff1f6;
  --head-ink:#5a4f00;
}
*{box-sizing:border-box;margin:0;padding:0}
html,body{width:1200px;height:1000px;overflow:hidden}
body{background:var(--ground);font-family:"Nunito Sans",Arial,sans-serif;color:var(--ink);position:relative}
.sheet{position:absolute;background:var(--paper);overflow:hidden;box-shadow:0 3px 8px rgba(0,0,0,.18)}
.abs{position:absolute;white-space:nowrap}
.brand-tab{position:absolute;left:0;background:var(--teal);border-radius:0 40px 40px 0;display:flex;align-items:center}
.brand-name{color:var(--yellow);font-weight:800;letter-spacing:.5px}
.title-bar{position:absolute;background:var(--teal);color:#fff;font-weight:700;text-align:center;white-space:nowrap}
.field{position:absolute;white-space:nowrap;overflow:hidden;color:var(--ink)}
.frame{position:absolute;border:4px solid var(--teal);border-radius:12px;background:#fff;overflow:hidden}

/* main form */
.objectives .brand-tab{top:48px;width:210px;height:74px;padding-left:38px}
.objectives .brand-name{font-size:27px}
.objectives .title-bar{left:30px;top:138px;width:549px;height:28px;font-size:17px;line-height:28px}
.objectives .field{font-size:12px}
.obj-table{position:absolute;left:30px;top:229px;width:549px;height:611px;background:var(--teal);border-radius:12px}
.reason-head{position:absolute;left:4px;width:541px;height:16px;background:var(--yellow);font-size:11.5px;font-weight:700;color:var(--head-ink)}
.reason-head span{position:absolute;top:0}
.q-row{position:absolute;left:4px;width:541px;background:#fff;border-bottom:1px solid var(--rule)}
.q-row p{position:absolute;left:14px;top:12px;width:176px;font-size:9.5px;line-height:12px;color:var(--muted)}
.q-row::after{content:"";position:absolute;left:192px;top:0;bottom:0;border-left:1px solid var(--rule)}

/* small sheets */
.mini{font-size:4.5px;line-height:6px}
.mini .brand-tab{height:30px;padding-left:12px}
.mini .brand-name{font-size:11px}
.mini .title-bar{font-size:5.5px;height:10px;line-height:10px}
.sec-label{position:absolute;left:3px;font-size:4.5px;font-weight:700;color:var(--ink);white-space:nowrap}
.bar{position:absolute;left:0;right:0;height:6px;font-size:4px;font-weight:700;color:#fff;padding-left:3px;line-height:6px;background:var(--teal);white-space:nowrap;overflow:hidden}
.bar.yellow{background:var(--yellow);color:var(--ink)}
.bar.lime{background:var(--lime);color:var(--ink)}
.col-head{position:absolute;left:0;right:0;height:12px;background:var(--teal);font-size:4px;color:#fff}
.col-head span{position:absolute;top:1px;white-space:nowrap}
.vline{position:absolute;border-left:1px solid var(--rule)}
.hline{position:absolute;border-top:1px solid var(--rule)}
.tick{position:absolute;width:6px;height:5px;border:1px solid var(--teal);background:#fff}
.tick.inline{position:relative;display:inline-block;top:1px;margin:0 2px 0 1px}

/* stacked pages */
.under-sheet{position:absolute;background:var(--paper);box-shadow:0 3px 8px rgba(0,0,0,.18)}
.under-sheet .frame{border-width:3px;border-radius:8px}
.back-page{position:absolute;top:503px;width:272px;height:384px;background:var(--paper);box-shadow:-3px 0 6px rgba(0,0,0,.18);overflow:hidden;font-size:4.5px}
.back-panel{position:absolute;left:14px;right:8px;border:3px solid var(--teal);border-radius:8px;background:#fff}
.back-panel.tinted{background:var(--tint)}
.opt{position:absolute;left:236px;white-space:nowrap;color:var(--ink)}
.opt .tick{position:relative;display:inline-block;top:1px;margin-left:2px}
.line-box{position:absolute;left:232px;width:20px;height:5px;border:1px solid var(--rule);background:#fff}
</style>
</head>
<body>

<!-- Health Objectives form -->
<section class="sheet objectives" style="left:22px;top:58px;width:608px;height:860px">
  <div class="brand-tab"><span class="brand-name">VERDALIA</span></div>
  <h1 class="title-bar">Health Objectives</h1>
  <p class="field" style="left:32px;top:178px">Nutritionist’s name : ................................................</p>
  <p class="field" style="left:322px;top:178px">Client’s name : ............................................................</p>
  <p class="field" style="left:32px;top:204px">Store location : ..........................................................</p>
  <p class="field" style="left:322px;top:204px">Date of consultation : ..............................................</p>

  <div class="obj-table">
    <div class="reason-head" style="top:17px"><span style="left:14px">Reason 1</span><span style="left:207px">Your comments</span></div>
    <div class="q-row" style="top:33px;height:66px"><p>Symptom, issue or condition you want to address.</p></div>
    <div class="q-row" style="top:99px;height:66px"><p>Duration - how long have you felt like this or experienced this symptom(s)?</p></div>
    <div class="q-row" style="top:165px;height:66px"><p>Have you seen a doctor about this for a diagnosis? Did you receive any medical treatment?</p></div>
    <div class="q-row" style="top:231px;height:68px"><p>Is there any background or extra health or lifestyle information that relates to this situation that you want your practitioner to know about? Please give details.</p></div>
    <div class="reason-head" style="top:311px"><span style="left:14px">Reason 2</span><span style="left:207px">Your comments</span></div>
    <div class="q-row" style="top:327px;height:66px"><p>Symptom, issue or condition you want to address.</p></div>
    <div class="q-row" style="top:393px;height:66px"><p>Duration - how long have you felt like this or experienced this symptom(s)?</p></div>
    <div class="q-row" style="top:459px;height:66px"><p>Have you seen a doctor about this for a diagnosis? Did you receive any medical treatment?</p></div>
    <div class="q-row" style="top:525px;height:70px"><p>Is there any background or extra health or lifestyle information that relates to this situation that you want to practitioner to know about? Please give details.</p></div>
  </div>
</section>

<!-- Pages beneath the consultation report -->
<div class="under-sheet" style="left:657px;top:110px;width:242px;height:345px;transform:rotate(-1.5deg)">
  <div class="frame" style="left:10px;top:290px;width:220px;height:48px;background:#fdfbe8"></div>
</div>
<div class="under-sheet" style="left:916px;top:110px;width:240px;height:362px;transform:rotate(2deg)">
  <div class="frame" style="left:12px;top:300px;width:216px;height:55px"></div>
</div>

<!-- Consultation Report, page 1 -->
<section class="sheet mini" style="left:653px;top:88px;width:242px;height:340px">
  <div class="brand-tab" style="top:20px;width:84px"><span class="brand-name">VERDALIA</span></div>
  <h2 class="title-bar" style="left:10px;top:55px;width:220px">Nutritional Therapy Consultation Report</h2>
  <p class="field" style="left:12px;top:69px">Nutritionist’s name : ..............................</p>
  <p class="field" style="left:127px;top:69px">Client’s name : ..............................</p>
  <p class="field" style="left:12px;top:80px">Consultation date : ..............................</p>
  <p class="field" style="left:127px;top:80px">Date of birth : ..............................</p>
  <p class="field" style="left:12px;top:91px">Store Location : ..............................</p>
  <p class="field" style="left:127px;top:91px">Current energy rating out of 10 : ..........</p>
  <div class="frame" style="left:12px;top:98px;width:218px;height:66px"><span class="sec-label" style="top:2px">General comments on your food diary</span></div>
  <div class="frame" style="left:12px;top:164px;width:218px;height:168px;border-radius:10px">
    <div class="bar" style="top:0">FOOD / DRINK TO HAVE MORE OF</div>
    <div class="col-head" style="top:6px"><span style="left:3px">Food / drink</span><span style="left:76px">Reason</span><span style="left:150px;white-space:normal;width:58px">How often should I have this food / drink?</span></div>
    <div class="vline" style="left:72px;top:18px;height:62px"></div><div class="vline" style="left:146px;top:18px;height:62px"></div>
    <div class="bar" style="top:82px">FOOD / DRINK TO HAVE LESS OF</div>
    <div class="col-head" style="top:88px"><span style="left:3px">Food / drink</span><span style="left:76px">Reason</span><span style="left:150px;white-space:normal;width:58px">How often can I have this food / drink?</span></div>
    <div class="vline" style="left:72px;top:100px;height:62px"></div><div class="vline" style="left:146px;top:100px;height:62px"></div>
  </div>
</section>

<!-- Consultation Report, page 2 -->
<section class="sheet mini" style="left:913px;top:88px;width:240px;height:340px">
  <h2 class="title-bar" style="left:12px;top:8px;width:216px">Nutritional Therapy Consultation Report</h2>
  <div class="frame" style="left:12px;top:16px;width:216px;height:76px"><span class="sec-label" style="top:2px">Food preparation advice:</span></div>
  <div class="frame" style="left:12px;top:92px;width:216px;height:74px;border-radius:8px">
    <div class="bar yellow" style="top:0">SUPPLEMENT PLAN</div>
    <div class="col-head" style="top:6px;height:7px"><span style="left:3px">Supplement</span><span style="left:68px">Brand</span><span style="left:112px">Dosage</span><span style="left:155px">When to take</span></div>
    <div class="vline" style="left:64px;top:13px;height:55px"></div><div class="vline" style="left:108px;top:13px;height:55px"></div><div class="vline" style="left:150px;top:13px;height:55px"></div>
  </div>
  <div class="frame" style="left:12px;top:166px;width:216px;height:76px"><span class="sec-label" style="top:2px">Suggested lifestyle changes:</span></div>
  <div class="frame" style="left:12px;top:242px;width:216px;height:90px"><span class="sec-label" style="top:2px">Personal message / any other comments:</span></div>
</section>

<!-- Consultation Form: following pages, back to front -->
<div class="back-page" style="left:883px">
  <div class="back-panel tinted" style="top:14px;height:355px"></div>
  <span class="abs" style="left:226px;top:36px">you can</span>
  <span class="line-box" style="top:40px"></span><span class="line-box" style="top:100px"></span>
  <span class="abs" style="left:234px;top:118px">ck</span>
  <span class="line-box" style="top:166px"></span><span class="line-box" style="top:180px"></span>
  <span class="opt" style="top:196px">No<span class="tick"></span></span>
  <span class="opt" style="top:204px">No<span class="tick"></span></span>
</div>
<div class="back-page" style="left:838px">
  <div class="back-panel" style="top:12px;height:196px"></div>
  <div class="back-panel" style="top:212px;height:60px"></div>
  <div class="back-panel" style="top:276px;height:50px"></div>
  <div class="back-panel" style="top:330px;height:46px"></div>
  <span class="opt" style="top:38px">No<span class="tick"></span></span>
  <span class="opt" style="top:48px">No<span class="tick"></span></span>
  <span class="opt" style="top:58px">No<span class="tick"></span></span>
  <span class="opt" style="top:68px">No<span class="tick"></span></span>
  <span class="opt" style="top:78px">No<span class="tick"></span></span>
  <span class="opt" style="top:96px">No<span class="tick"></span></span>
  <span class="opt" style="top:106px">No<span class="tick"></span></span>
  <span class="opt" style="top:118px">No<span class="tick"></span></span>
  <span class="opt" style="top:130px">No<span class="tick"></span></span>
  <span class="opt" style="top:154px">No<span class="tick"></span></span>
  <span class="opt" style="top:166px">No<span class="tick"></span></span>
  <span class="opt" style="top:186px">No<span class="tick"></span></span>
  <span class="opt" style="top:236px">No<span class="tick"></span></span>
  <span class="opt" style="top:246px">No<span class="tick"></span></span>
  <span class="opt" style="top:296px">No<span class="tick"></span></span>
  <span class="opt" style="top:312px">No<span class="tick"></span></span>
  <span class="opt" style="top:340px">No<span class="tick"></span></span>
  <span class="opt" style="top:356px">No<span class="tick"></span></span>
</div>
<div class="back-page" style="left:793px">
  <div class="back-panel" style="top:12px;height:100px"></div>
  <div class="back-panel" style="top:116px;height:56px"></div>
  <div class="back-panel" style="top:176px;height:80px"></div>
  <div class="back-panel" style="top:262px;height:114px"></div>
  <span class="opt" style="top:36px">No<span class="tick"></span></span>
  <span class="opt" style="top:46px">No<span class="tick"></span></span>
  <span class="opt" style="top:56px">No<span class="tick"></span></span>
  <span class="opt" style="top:66px">No<span class="tick"></span></span>
  <span class="opt" style="top:80px">No<span class="tick"></span></span>
  <span class="opt" style="top:90px">No<span class="tick"></span></span>
  <span class="opt" style="top:140px">No<span class="tick"></span></span>
  <span class="opt" style="top:150px">No<span class="tick"></span></span>
  <span class="opt" style="top:236px">No<span class="tick"></span></span>
  <span class="opt" style="top:246px">No<span class="tick"></span></span>
  <span class="opt" style="top:286px">No<span class="tick"></span></span>
  <span class="opt" style="top:300px">No<span class="tick"></span></span>
  <span class="opt" style="top:328px">No<span class="tick"></span></span>
  <span class="opt" style="top:344px">No<span class="tick"></span></span>
  <span class="opt" style="top:358px">No<span class="tick"></span></span>
</div>
<div class="back-page" style="left:748px">
  <div class="back-panel" style="top:12px;height:106px"></div>
  <div class="back-panel" style="top:124px;height:62px"></div>
  <div class="back-panel" style="top:192px;height:74px"></div>
  <div class="back-panel" style="top:272px;height:104px"></div>
  <span class="opt" style="top:38px">No<span class="tick"></span></span>
  <span class="opt" style="top:52px">No<span class="tick"></span></span>
  <span class="opt" style="top:66px">No<span class="tick"></span></span>
  <span class="opt" style="top:146px">No<span class="tick"></span></span>
  <span class="opt" style="top:160px">No<span class="tick"></span></span>
  <span class="abs" style="left:230px;top:234px">ts or</span>
  <span class="opt" style="top:246px">No<span class="tick"></span></span>
  <span class="opt" style="top:320px">No<span class="tick"></span></span>
</div>
<div class="back-page" style="left:703px">
  <div class="back-panel" style="top:8px;height:368px"></div>
</div>

<!-- Consultation Form: first page -->
<section class="sheet mini" style="left:653px;top:503px;width:272px;height:384px">
  <div class="brand-tab" style="top:21px;width:94px;height:32px"><span class="brand-name">VERDALIA</span></div>
  <h2 class="title-bar" style="left:14px;top:58px;width:246px;font-weight:400">Nutritional Therapy Consultation Form</h2>
  <p class="field" style="left:14px;top:74px">Nutritionist’s name : ..............................</p>
  <p class="field" style="left:14px;top:86px">Store location : ..............................</p>
  <p class="field" style="left:144px;top:86px">Date of consultation : ..........................</p>
  <div class="frame" style="left:14px;top:98px;width:246px;height:268px;border-width:3px;border-radius:8px">
    <div class="abs" style="left:0;top:0;width:240px;height:90px;background:var(--tint)">
      <span class="sec-label" style="top:2px">Customer details</span>
      <span class="abs" style="left:6px;top:10px;line-height:7.6px">Name :<br>Date of birth :<br>Occupation :<br>Height :<br>Weight :<br>Phone number :<br>Email address :<br>Address :</span>
      <span class="abs" style="left:44px;top:10px;width:90px;height:52px;background:repeating-linear-gradient(#fff 0 6px,transparent 6px 7.6px)"></span>
      <span class="abs" style="left:44px;top:63px;width:192px;height:22px;background:#fff"></span>
      <span class="abs" style="left:170px;top:10px">Sex M<span class="tick inline"></span> F<span class="tick inline"></span></span>
      <span class="abs" style="left:172px;top:20px;line-height:7.5px">Only for women<br>Are you currently pregnant?<br>Are you currently breastfeeding?</span>
      <span class="abs" style="left:224px;top:27px;line-height:7.5px">Y<br>Y</span>
      <span class="tick" style="left:229px;top:28px"></span><span class="tick" style="left:229px;top:35px"></span>
    </div>
    <div class="bar yellow" style="top:92px;height:8px;line-height:8px">Please provide details of any medications prescribed by your doctor / consultant that you are currently taking :</div>
    <span class="abs" style="left:3px;top:106px">Name of medication</span><span class="abs" style="left:74px;top:106px">Reason for prescription</span><span class="abs" style="left:176px;top:102px;width:60px;white-space:normal">How long have you been taking this medication?</span>
    <div class="vline" style="left:70px;top:101px;height:58px"></div><div class="vline" style="left:172px;top:101px;height:58px"></div>
    <div class="hline" style="left:0;right:0;top:116px"></div><div class="hline" style="left:0;right:0;top:128px"></div><div class="hline" style="left:0;right:0;top:140px"></div>
    <div class="bar yellow" style="top:162px;height:8px;line-height:8px">Please provide details of any nutritional supplements or herbal medicines that you are currently taking :</div>
    <div class="bar lime" style="top:172px;height:9px;line-height:9px"><span>Name of supplement / herb</span><span style="position:absolute;left:74px">Reason for use</span><span style="position:absolute;left:176px">How long have you been taking this?</span></div>
    <div class="vline" style="left:70px;top:181px;height:40px"></div><div class="vline" style="left:172px;top:181px;height:40px"></div>
    <div class="hline" style="left:0;right:0;top:193px"></div><div class="hline" style="left:0;right:0;top:205px"></div>
    <div class="hline" style="left:0;right:0;top:224px;border-top:3px solid var(--teal)"></div>
    <span class="abs" style="left:6px;top:230px;width:228px;white-space:normal">What is the reason you are seeking nutritional support? Please only give a brief comment here as further information will be requested during your consultation.</span>
  </div>
</section>

</body>
</html>
```